Brightvale Advisory Inc. (Enterprise Resource Planning - All KRT)

I need a logo and business card design for an Brightvale Advisory company based in Dallas, We specifically provide consulting services for implementing and maintaining KRT ERP systems, I would like to see all the colors be navy and white. White Card on one side with Navy print, and Navy card on the other side with White print. The design should communicate that we "Prevail" results by effort, skill and courage.

Target Market(s)

Meridian 400 companies that are implementing or maintaining an KRT ERP system. My specialty is Finance and Controlling

Industry/Entity Type

Business Consultant

Contact Information for Business Card

Dana Holbrook
President / CEO

2380 Wrenfield Lane
Corwin Falls, Oregon 75341

Tel: 472-583-0972
eMail: dana.holbrook@brightvaleadvisory.co
web: www.brightvaleadvisory.co

Logo Text

This needs to be a Graphic Design

Font styles to use
Sans Serif

Colors
0555a3
ffffff

Requirements
Must have
• two sided
• Front side - Navy card with white print
• name, title, telephone, email
• Back side - White card with navy print
• street address, web address,
• Slogan [Prevail ~ Grit, Insight, and Resolve}
Nice to have
• Classic and Clean
Should not have
• typical IT stuff... we are a consulting service organization not an IT department.

```html
<!DOCTYPE html>
<html lang="en">
<head>
<meta charset="utf-8">
<title>Brightvale Advisory — Business Card</title>
<link href="https://fonts.googleapis.com/css2?family=Mulish:ital,wght@0,400;0,500;0,800;1,500&display=swap" rel="stylesheet">
<style>
  :root {
    --navy: #282f6b;
    --white: #f1f1f1;
    --ink-white: #ffffff;
    --backdrop: #e6e4e0;
    --rule-light: rgba(255,255,255,0.65);
  }
  * { margin: 0; padding: 0; box-sizing: border-box; }
  html, body { width: 1200px; height: 1200px; overflow: hidden; }
  body {
    background: var(--backdrop);
    font-family: "Mulish", sans-serif;
    position: relative;
  }
  .card {
    position: absolute;
    left: 282px;
    width: 630px;
    height: 360px;
    box-shadow: 0 2px 6px rgba(0,0,0,0.18);
  }
  .card--back { top: 214px; background: var(--white); color: var(--navy); }
  .card--front { top: 608px; background: var(--navy); color: var(--ink-white); }

  .wordmark {
    position: absolute;
    display: flex;
    align-items: center;
    gap: 18px;
  }
  .wordmark__dot {
    width: 64px; height: 64px;
    border-radius: 50%;
    border: 2px solid currentColor;
    flex: none;
  }
  .wordmark__name {
    font-weight: 500;
    font-size: 25px;
    letter-spacing: 0.28em;
    line-height: 1.35;
    text-transform: uppercase;
  }
  .card--back .wordmark { left: 0; right: 0; top: 62px; justify-content: center; }
  .card--front .wordmark { left: 48px; top: 54px; }

  .slogan {
    position: absolute;
    top: 228px; left: 0; right: 0;
    text-align: center;
    font-style: italic;
    font-weight: 500;
    font-size: 18px;
  }
  .web-line {
    position: absolute;
    left: 46px; top: 312px;
    width: 304px; height: 1px;
    background: var(--navy);
  }
  .web-line::after {
    content: "";
    position: absolute; right: -2px; top: -2px;
    width: 5px; height: 5px; border-radius: 50%;
    background: var(--navy);
  }
  .web-address {
    position: absolute;
    right: 46px; top: 302px;
    font-size: 16px; font-weight: 500;
    letter-spacing: 0.03em;
  }

  .person { position: absolute; right: 46px; top: 196px; text-align: right; }
  .person__name { font-weight: 800; font-size: 23px; line-height: 1.2; }
  .person__title { font-size: 15px; letter-spacing: 0.02em; margin-top: 2px; }
  .divider {
    position: absolute; left: 46px; right: 46px; top: 261px;
    height: 1px; background: var(--rule-light);
  }
  .contact { position: absolute; left: 46px; top: 274px; list-style: none; font-size: 15.5px; letter-spacing: 0.02em; }
  .contact li { display: flex; align-items: center; gap: 12px; height: 26px; }
  .contact svg { width: 17px; height: 17px; flex: none; }
  .address {
    position: absolute; right: 46px; top: 277px;
    text-align: right; font-size: 15.5px; line-height: 21px; font-style: normal;
    letter-spacing: 0.02em;
  }
</style>
</head>
<body>

<section class="card card--back">
  <div class="wordmark">
    <span class="wordmark__dot"></span>
    <span class="wordmark__name">Brightvale<br>Advisory</span>
  </div>
  <p class="slogan">Prevail ~ Grit, Insight, and Resolve</p>
  <span class="web-line"></span>
  <p class="web-address">www.brightvaleadvisory.co</p>
</section>

<section class="card card--front">
  <div class="wordmark">
    <span class="wordmark__dot"></span>
    <span class="wordmark__name">Brightvale<br>Advisory</span>
  </div>
  <div class="person">
    <p class="person__name">Dana Holbrook</p>
    <p class="person__title">President / CEO</p>
  </div>
  <span class="divider"></span>
  <ul class="contact">
    <li>
      <svg viewBox="0 0 20 20" aria-hidden="true"><circle cx="10" cy="10" r="9" fill="none" stroke="#fff" stroke-width="1.3"/><path d="M7 5.5l1.6 2.2-1 1.1c.6 1.3 1.5 2.2 2.7 2.8l1.1-1 2.1 1.6-.9 1.5c-3.3-.3-6-3-6.3-6.4z" fill="#fff"/></svg>
      472-583-0972
    </li>
    <li>
      <svg viewBox="0 0 20 20" aria-hidden="true"><circle cx="10" cy="10" r="9" fill="none" stroke="#fff" stroke-width="1.3"/><rect x="5.5" y="7" width="9" height="6.3" fill="#fff"/><path d="M5.5 7l4.5 3.5L14.5 7" fill="none" stroke="#282f6b" stroke-width="1"/></svg>
      dana.holbrook@brightvaleadvisory.co
    </li>
  </ul>
  <address class="address">2380 Wrenfield Lane<br>Corwin Falls, Oregon 75341</address>
</section>

</body>
</html>
```